Veterinary TPLO Surgery Flyer Design

Please use this flyer to make a professional-looking 1 page, double-sided client handout regarding TPLO.

You can visit our website at www.brackenfieldpetcare.com & www.northwoodsanimalsurgerygroup.com for additional logo information. The flyer should include all the text from the one provided.

Target Market(s)

Client communication to for referral surgery between sister veterinary clinics

Industry/Entity Type

Veterinary

Requirements
Must have
• The text included
Nice to have
• Nice to have the Cedar Hollow Avenue Animal CLinic & Dr. Pell Mobile vet logos incorporated.

```html
<!DOCTYPE html>
<html lang="en">
<head>
<meta charset="utf-8">
<title>TPLO Surgery Client Handout</title>
<link href="https://fonts.googleapis.com/css2?family=Fira+Sans:wght@500;600;700&family=Lato:wght@400;700&display=swap" rel="stylesheet">
<style>
:root{
  --backdrop:#7b7b7b;
  --green:#5f8c6c;
  --green-dark:#3f7a55;
  --heading-green:#4c8a5c;
  --yellow:#f2d54a;
  --tan:#7d7049;
  --tan-strip:#a8996a;
  --navy:#1e3c78;
  --ink:#2b2b2b;
  --white:#ffffff;
}
*{margin:0;padding:0;box-sizing:border-box}
html,body{width:1200px;height:904px;overflow:hidden;background:var(--backdrop)}
body{position:relative;font-family:'Lato',sans-serif;color:var(--ink)}
.page{position:absolute;width:452px;height:585px;background:var(--white);overflow:hidden;box-shadow:0 4px 14px rgba(0,0,0,.35)}
.page--front{left:139px;top:61px}
.page--back{left:628px;top:274px}
.abs{position:absolute}
h2,h3,h4{font-family:'Fira Sans',sans-serif}
p{font-size:7.6px;line-height:10.6px;text-align:justify}

/* front */
.hero{left:0;top:0;width:452px;height:226px;background:linear-gradient(120deg,#3f4a18 0%,#6f7d2a 40%,#a3a046 70%,#5e6f24 100%)}
.brand{left:25px;top:21px;display:flex;align-items:center;gap:6px;color:var(--white);font-family:'Fira Sans',sans-serif;font-weight:500;font-size:15px;line-height:17px}
.brand__dot{width:30px;height:30px;border-radius:50%;background:var(--white);opacity:.9;flex:none}
.hero__title{left:25px;top:82px;width:210px;color:var(--white);font-family:'Fira Sans',sans-serif;font-weight:700;font-size:11.8px;line-height:15.3px}
.about{left:0;top:176px;width:235px;height:401px;background:var(--green);border-top-right-radius:18px;border-top:4px solid var(--white);border-right:4px solid var(--white)}
.about__heading{left:25px;top:20px;color:var(--yellow);font-size:16px;font-weight:700}
.about__text{left:25px;top:47px;width:190px;color:var(--white)}
.about__text p{text-align:left}
.portrait{left:132px;top:44px;width:88px;height:88px;border-radius:50%;border:4px solid var(--white);background:radial-gradient(circle at 50% 45%,#d9b06a,#8e6a2e)}
.why{left:26px;top:216px;width:189px;height:166px;background:var(--tan);border:3px solid var(--white);padding:14px 12px 0 12px;color:var(--white)}
.why h3{color:var(--yellow);font-size:9.6px;line-height:12.4px;font-weight:700}
.why p{margin-top:2px;font-size:7.5px;line-height:10.2px;font-weight:700}
.col{left:251px;width:174px}
.col h2{color:var(--heading-green);font-size:13px;font-weight:700}
.xray{top:334px;width:84px;height:71px}
.benefit{left:251px;width:180px;display:flex;gap:9px}
.benefit svg{flex:none}
.benefit h4{font-size:7.8px;font-weight:700;color:var(--ink);line-height:10px}
.benefit p{font-size:7.4px;line-height:9.8px;text-align:left}
.strip{top:577px;height:8px}

/* back */
.back-green{left:215px;top:0;width:237px;height:336px;background:var(--green)}
.back-col{left:27px;top:26px;width:170px}
.back-col h2{color:var(--heading-green);font-size:11.2px;line-height:14px;font-weight:600}
.back-col .sub{color:var(--navy);font-family:'Fira Sans',sans-serif;font-size:10px;line-height:12.5px;font-weight:500}
.back-col p{font-size:8px;line-height:10.8px}
.back-col h4{font-size:8.2px;margin-top:6px;font-weight:600}
.process{left:234px;top:24px;color:var(--white);font-size:13px;font-weight:700}
.step{left:237px;width:205px;display:flex;align-items:flex-start;gap:8px;color:var(--white)}
.step__num{flex:none;width:24px;height:24px;border-radius:50%;background:var(--yellow);border:2px solid var(--white);color:var(--green-dark);font-family:'Fira Sans',sans-serif;font-weight:700;font-size:15px;display:flex;align-items:center;justify-content:center}
.step p{font-size:7.3px;line-height:9.7px;text-align:left;padding-top:1px}
.building{left:0;top:336px;width:452px;height:144px;background:linear-gradient(180deg,#8fa0a8 0%,#7a6f62 45%,#5c6b45 100%)}
.badge{left:395px;top:338px;width:80px;height:80px;border-radius:50%;background:#c9d4de;border:2px solid #3f5e8a}
.contact-tab{left:152px;top:482px;width:148px;height:16px;background:var(--green);clip-path:polygon(0 0,100% 0,92% 100%,8% 100%);color:var(--white);font-family:'Fira Sans',sans-serif;font-weight:700;font-size:8.4px;text-align:center;line-height:16px}
.contact-rule{left:0;top:480px;width:452px;height:2px;background:var(--green)}
.contact-brand{left:23px;top:495px;display:flex;align-items:center;gap:4px;color:var(--ink);font-family:'Fira Sans',sans-serif;font-weight:500;font-size:10.5px;line-height:11.5px}
.contact-brand__dot{width:19px;height:19px;border-radius:50%;background:var(--green);flex:none}
.contact-name{color:var(--heading-green);font-size:10px;line-height:12px;font-weight:700}
.line{display:flex;align-items:center;gap:4px;font-size:7.7px;line-height:12.4px;white-space:nowrap}
.divider{left:225px;top:512px;width:1.5px;height:58px;background:var(--green)}
.partner{left:366px;top:497px;display:flex;flex-direction:column;align-items:center;gap:2px;width:60px}
.partner__dot{width:26px;height:26px;border-radius:50%;background:var(--green)}
.partner__name{font-size:6.5px;font-weight:700;color:var(--navy);text-align:center}
.back-strip{left:0;top:580px;width:452px;height:5px;background:var(--green)}
</style>
</head>
<body>
<svg width="0" height="0" style="position:absolute">
  <defs>
    <symbol id="ico-pin" viewBox="0 0 10 10"><circle cx="5" cy="5" r="5" fill="#5f8c6c"/><path d="M5 2.2a1.8 1.8 0 0 1 1.8 1.8C6.8 5.4 5 7.8 5 7.8S3.2 5.4 3.2 4A1.8 1.8 0 0 1 5 2.2z" fill="#fff"/></symbol>
    <symbol id="ico-phone" viewBox="0 0 10 10"><circle cx="5" cy="5" r="5" fill="#5f8c6c"/><path d="M3.2 2.5l1 .1.4 1.3-.6.5a4 4 0 0 0 1.6 1.6l.5-.6 1.3.4.1 1c-2.7.4-4.7-1.6-4.3-4.3z" fill="#fff"/></symbol>
    <symbol id="ico-mail" viewBox="0 0 10 10"><circle cx="5" cy="5" r="5" fill="#5f8c6c"/><rect x="2.4" y="3.2" width="5.2" height="3.6" fill="#fff"/><path d="M2.4 3.2L5 5.3 7.6 3.2" stroke="#5f8c6c" stroke-width=".6" fill="none"/></symbol>
    <symbol id="ico-web" viewBox="0 0 10 10"><circle cx="5" cy="5" r="5" fill="#5f8c6c"/><circle cx="5" cy="5" r="2.8" fill="none" stroke="#fff" stroke-width=".6"/><path d="M2.2 5h5.6M5 2.2v5.6" stroke="#fff" stroke-width=".6"/></symbol>
    <symbol id="shield" viewBox="0 0 28 34"><path d="M2 2h24v16c0 7-6 11-12 14C8 29 2 25 2 18z" fill="#4c8a5c" stroke="#9bb9a4" stroke-width="1.5"/><circle cx="14" cy="15" r="6" fill="none" stroke="#fff" stroke-width="1.4"/></symbol>
  </defs>
</svg>

<!-- Front side -->
<section class="page page--front">
  <div class="abs hero" role="img" aria-label="Photo of a brown Labrador sitting on grass facing a small child holding a pink flying disc"></div>
  <div class="abs brand"><span class="brand__dot"></span><span>Cedar Hollow Avenue<br>Animal Clinic</span></div>
  <h1 class="abs hero__title">ADVANCED ORTHOPEDIC CARE by Dr. Helena Pell, DVM, DACVS-sa TPLO Surgery at Cedar Hollow Avenue Animal Clinic</h1>

  <div class="abs about">
    <h2 class="abs about__heading">About Dr. Helena Pell</h2>
    <div class="abs portrait" role="img" aria-label="Portrait photo of Dr. Helena Pell"></div>
    <div class="abs about__text">
      <p style="width:104px">Dr. Helena Pell is a board-certified veterinary surgeon (Diplomate of the American College of Veterinary Surgeons) with over 18 years of experience in small animal surgery. A graduate of Great Lakes State</p>
      <p>University, she completed her surgical residency at Eastbrook School of Veterinary Medicine. Through her mobile practice, <b>Pell Surgical Services</b>, Dr. Pell now provides advanced surgical procedures—such as TPLO—directly at local clinics.</p>
    </div>
    <div class="abs why">
      <h3>WHY CHOOSE<br>Cedar Hollow Avenue Animal Clinic?</h3>
      <p>Partnering with Dr. Pell, Cedar Hollow Avenue Animal Clinic offers advanced orthopedic surgery on-site—eliminating the need for referrals or travel. This collaboration ensures your pet receives expert surgical care in a familiar, trusted environment. Our clinic works directly with your primary veterinarian to share medical records, diagnostics, and prescriptions, ensuring seamless &amp; coordinated care for your pet.</p>
    </div>
  </div>

  <div class="abs col" style="top:240px">
    <h2>What is TPLO Surgery?</h2>
    <p style="margin-top:3px;font-size:7.4px;line-height:9.9px"><b>Tibial Plateau Leveling Osteotomy (TPLO)</b> is a surgical procedure that stabilizes the stifle (knee) joint following a <b>cranial cruciate ligament (CCL)</b> rupture—a common orthopedic injury in dogs. The procedure involves altering the angle of the tibial plateau to eliminate abnormal joint motion, restoring stability and improving function.</p>
  </div>
  <div class="abs xray" style="left:251px;background:linear-gradient(135deg,#1a1a1a,#5a5a5a 50%,#1e1e1e)" role="img" aria-label="Pre- and post-operative TPLO radiographs of a dog's knee"></div>
  <div class="abs xray" style="left:341px;background:linear-gradient(135deg,#c9c6bd,#e6e2d6 50%,#b8b6b0)" role="img" aria-label="Diagram of the tibial plateau angle before and after TPLO"></div>

  <h2 class="abs" style="left:251px;top:425px;color:var(--heading-green);font-size:10px;font-weight:600">Benefits of TPLO Surgery</h2>
  <div class="abs benefit" style="top:441px"><svg width="28" height="34"><use href="#shield"/></svg><div><h4>Enhanced Joint Stability:</h4><p>Restores natural biomechanics, reducing pain &amp; improving mobility.</p></div></div>
  <div class="abs benefit" style="top:480px"><svg width="28" height="34"><use href="#shield"/></svg><div><h4>Faster Recovery:</h4><p>Many dogs return to normal activity faster compared to other surgical techniques.</p></div></div>
  <div class="abs benefit" style="top:525px"><svg width="28" height="34"><use href="#shield"/></svg><div><h4>Proven Long-Term Success:</h4><p>TPLO is particularly effective in large and active breeds.</p></div></div>

  <div class="abs strip" style="left:0;width:235px;background:var(--tan-strip)"></div>
  <div class="abs strip" style="left:235px;width:217px;background:var(--green)"></div>
</section>

<!-- Back side -->
<section class="page page--back">
  <div class="abs back-green"></div>
  <div class="abs back-col">
    <h2>Diagnostic Radiographs vs.<br>TPLO Planning Radiographs</h2>
    <p style="margin-top:7px">While diagnostic radiographs may confirm a CCL tear, <b>they are not sufficient for surgical planning.</b> TPLO requires <b>three advanced technique radiographic views</b> with precise measurements, which must be performed under sedation to reduce discomfort and allow accurate positioning.</p>
    <h2 style="margin-top:14px;font-size:10px;line-height:12px">Post-Operative Care &amp; Follow-Up</h2>
    <div class="sub">Two follow-up appointments will be scheduled:</div>
    <h4>4 Weeks Post-Op:</h4>
    <p>Evaluate healing, refill medications, and address any questions.</p>
    <h4>8 Weeks Post-Op:</h4>
    <p>Sedated radiographs will confirm proper healing of the surgical site and tibia.</p>
    <p style="margin-top:4px">Dr. Pell will stay in direct contact with you during your pet's recovery using her custom <b>mobile app</b>, which allows for secure messaging and provides detailed post-operative instructions.</p>
  </div>

  <h2 class="abs process">Expected Process</h2>
  <div class="abs step" style="top:44px"><span class="step__num">1</span><p><b>Diagnosis:</b> Your pet is diagnosed with stifle instability (CCL tear) by your veterinarian.</p></div>
  <div class="abs step" style="top:73px"><span class="step__num">2</span><p><b>Referral:</b> Your veterinarian contacts the surgical coordinator at Cedar Hollow Avenue Animal Clinic.</p></div>
  <div class="abs step" style="top:101px"><span class="step__num">3</span><p><b>Consultation:</b> The coordinator contacts you to schedule a 1-hour consultation to review the procedure, estimated costs, and available surgery dates.</p></div>
  <div class="abs step" style="top:148px"><span class="step__num">4</span><p><b>Planning Radiographs:</b> These specialized X-rays are typically taken during the consultation under light sedation.</p></div>
  <div class="abs step" style="top:186px"><span class="step__num">5</span><p><b>Surgical Review:</b> Dr. Pell reviews the radiographs and your pet's medical history to confirm candidacy for TPLO.</p></div>
  <div class="abs step" style="top:224px"><span class="step__num">6</span><p><b>Deposit:</b> A $3,500 deposit secures Dr. Pell's travel and surgery date. This is refundable if canceled at least 5 days prior to the scheduled procedure.</p></div>
  <div class="abs step" style="top:268px"><span class="step__num">7</span><p><b>Surgery Day:</b> Your pet is dropped off in the morning &amp; surgery is performed the same day.</p></div>
  <div class="abs step" style="top:296px"><span class="step__num">8</span><p><b>Discharge:</b> You'll receive a post-surgery update &amp; your pet will go home that evening.</p></div>

  <div class="abs building" role="img" aria-label="Photo of the clinic building exterior with its roadside sign"></div>
  <div class="abs badge"></div>

  <div class="abs contact-rule"></div>
  <div class="abs contact-tab">CONTACT INFORMATION:</div>

  <div class="abs contact-brand"><span class="contact-brand__dot"></span><span>Cedar Hollow Avenue<br>Animal Clinic</span></div>
  <div class="abs" style="left:26px;top:523px">
    <h3 class="contact-name">Cedar Hollow Avenue Animal Clinic</h3>
    <div class="line"><svg width="9" height="9"><use href="#ico-pin"/></svg>2280 Cedar Hollow Avenue, Brackenfield, MI 48000</div>
    <div class="line"><svg width="9" height="9"><use href="#ico-phone"/></svg>(555) 214-8031 &nbsp;&nbsp;<svg width="9" height="9"><use href="#ico-mail"/></svg>info@brackenfieldpetcare.com</div>
    <div class="line"><svg width="9" height="9"><use href="#ico-web"/></svg>www.brackenfieldpetcare.com</div>
  </div>

  <div class="abs divider"></div>

  <div class="abs" style="left:236px;top:511px">
    <h3 class="contact-name">Pell Surgical Services<br>(Dr. Helena Pell)</h3>
    <div class="line"><svg width="9" height="9"><use href="#ico-phone"/></svg>(555) 390-6826</div>
    <div class="line"><svg width="9" height="9"><use href="#ico-mail"/></svg>drpell@northwoodsanimalsurgerygroup.com</div>
    <div class="line"><svg width="9" height="9"><use href="#ico-web"/></svg>www.northwoodsanimalsurgerygroup.com</div>
  </div>
  <div class="abs partner"><span class="partner__dot"></span><span class="partner__name">Helena Pell</span></div>

  <div class="abs back-strip"></div>
</section>
</body>
</html>
```